Business Cards for a law firm

Business cards for our law firm. Use our silhoette logo and OAK HARBOR - check our website (www.oakharbor-legal.com)

Contact Information for Business Card

our silhouette logo, OAK HARBOR, 800-555-0147, Dorian Kestrup, dorian@oakharbor-legal.com

Requirements
Must have
• our silhouette logo, OAK HARBOR, 800-555-0147, Dorian Kestrup, dorian@oakharbor-legal.com

```html
<!DOCTYPE html>
<html lang="en">
<head>
<meta charset="utf-8">
<title>Oak Harbor — Business Cards</title>
<link rel="stylesheet" href="https://fonts.googleapis.com/css2?family=Raleway:wght@300;400;500;700&display=swap">
<style>
  :root {
    --navy: #1b2f6b;
    --orange: #f5a623;
    --white: #ffffff;
    --backdrop: #e9eaec;
    --divider: rgba(255,255,255,0.35);
  }
  * { box-sizing: border-box; margin: 0; padding: 0; }
  html, body { width: 1200px; height: 1200px; overflow: hidden; }
  body {
    background: var(--backdrop);
    font-family: "Raleway", sans-serif;
    display: flex;
    flex-direction: column;
    align-items: center;
    justify-content: center;
    gap: 58px;
  }
  .card {
    position: relative;
    width: 860px;
    height: 491px;
    border-radius: 38px;
    overflow: hidden;
    box-shadow: 0 10px 28px rgba(0,0,0,0.18);
  }

  /* Front side */
  .card--front { background: var(--white); }
  .card--front .brand-zone {
    position: absolute; left: 0; top: 0; width: 100%; height: 236px;
    display: flex; align-items: center; justify-content: center;
  }
  .wordmark {
    font-family: "Raleway", sans-serif;
    font-weight: 300;
    letter-spacing: 2px;
    line-height: 1;
    display: flex; align-items: center; gap: 22px;
  }
  .wordmark__dot { border-radius: 50%; flex: none; }
  .card--front .wordmark { color: var(--navy); font-size: 64px; }
  .card--front .wordmark__dot { width: 46px; height: 46px; background: var(--navy); }

  .accent-stripe {
    position: absolute; left: 0; top: 236px; width: 100%; height: 12px;
    background: var(--orange);
  }
  .info-band {
    position: absolute; left: 0; top: 248px; width: 100%; bottom: 0;
    background: var(--navy);
    display: flex; align-items: center;
    padding: 0 60px 0 80px;
  }
  .person { width: 330px; }
  .person__name {
    color: var(--orange); font-weight: 700; font-size: 34px;
    letter-spacing: 1px; text-transform: uppercase; line-height: 1.1;
  }
  .person__title {
    color: var(--white); font-weight: 400; font-size: 22px;
    letter-spacing: 1px; margin-top: 6px;
  }
  .info-divider {
    width: 1px; height: 120px; background: var(--divider); margin: 0 40px 0 20px;
  }
  .contact-list { list-style: none; display: flex; flex-direction: column; gap: 16px; }
  .contact-list li {
    display: flex; align-items: center; gap: 14px;
    color: var(--white); font-size: 22px; font-weight: 400; letter-spacing: 0.5px;
  }
  .contact-list svg { width: 26px; height: 26px; flex: none; }

  /* Back side */
  .card--back {
    background: var(--navy);
    display: flex; align-items: center; justify-content: center;
  }
  .card--back .wordmark { color: var(--white); font-size: 78px; }
  .card--back .wordmark__dot { width: 56px; height: 56px; background: var(--white); }
</style>
</head>
<body>

  <section class="card card--front" aria-label="Business card front">
    <div class="brand-zone">
      <div class="wordmark"><span class="wordmark__dot"></span>OAK HARBOR</div>
    </div>
    <div class="accent-stripe"></div>
    <div class="info-band">
      <div class="person">
        <p class="person__name">Dorian Kestrup</p>
        <p class="person__title">TITLE</p>
      </div>
      <div class="info-divider"></div>
      <ul class="contact-list">
        <li>
          <svg viewBox="0 0 24 24" aria-hidden="true"><path fill="var(--orange)" d="M6.6 10.8a15 15 0 0 0 6.6 6.6l2.2-2.2a1 1 0 0 1 1-.25 11.4 11.4 0 0 0 3.6.57 1 1 0 0 1 1 1V20a1 1 0 0 1-1 1A17 17 0 0 1 3 4a1 1 0 0 1 1-1h3.5a1 1 0 0 1 1 1c0 1.25.2 2.45.57 3.57a1 1 0 0 1-.25 1z"/></svg>
          800-555-0147
        </li>
        <li>
          <svg viewBox="0 0 24 24" aria-hidden="true"><rect x="2" y="5" width="20" height="14" rx="1.5" fill="var(--orange)"/><path d="M2.5 6l9.5 7 9.5-7" fill="none" stroke="var(--navy)" stroke-width="1.8"/></svg>
          dorian@oakharbor-legal.com
        </li>
        <li>
          <svg viewBox="0 0 24 24" aria-hidden="true" fill="none" stroke="var(--orange)" stroke-width="1.8"><circle cx="12" cy="12" r="9.5"/><ellipse cx="12" cy="12" rx="4.2" ry="9.5"/><path d="M2.5 12h19M4 7h16M4 17h16"/></svg>
          www.oakharbor-legal.com
        </li>
      </ul>
    </div>
  </section>

  <section class="card card--back" aria-label="Business card back">
    <div class="wordmark"><span class="wordmark__dot"></span>OAK HARBOR</div>
  </section>

</body>
</html>
```